Biz Cards for Lumivale Associates

Lumivale Associates is seeking a single-sided business card that is more visually-appealing than our current design (see attached).

Notes:
- Our colors are blue & teal.
- Our tag line must be large enough to be easily read
- We don't necessarily need our address included (that's just the biz office)
- We'd like to add our email address: Lumivale512@brindlemail.net

Thanks!

Industry/Entity Type

Business

Contact Information for Business Card

Standard size
PSD file required w/ text on its own layer

Colors
86cfc6
3277b5

```html
<!DOCTYPE html>
<html lang="en">
<head>
<meta charset="utf-8">
<title>Lumivale Associates — Business Card</title>
<link href="https://fonts.googleapis.com/css2?family=Roboto+Condensed:wght@400;500&family=Open+Sans:ital,wght@1,400&family=Roboto:wght@500&display=swap" rel="stylesheet">
<style>
  :root {
    --page-bg: #e4e6e8;
    --card-bg: #ffffff;
    --ink: #1c1c1c;
    --band-dark: #2b2b2b;
    --brand-blue: #3277b5;
    --brand-blue-light: #5f98cf;
    --brand-teal: #86cfc6;
    --tagline-blue: #2f6fb3;
    --white: #ffffff;
  }
  * { box-sizing: border-box; margin: 0; padding: 0; }
  html, body {
    width: 1200px; height: 1200px; overflow: hidden;
    background: var(--page-bg);
  }
  .card {
    position: absolute;
    left: 100px; top: 280px;
    width: 1000px; height: 640px;
    background: var(--card-bg);
    overflow: hidden;
    box-shadow: 0 8px 24px rgba(0,0,0,0.12);
  }
  .card__bands { position: absolute; inset: 0; }
  .brand {
    position: absolute; left: 0; right: 0; top: 60px;
    text-align: center;
  }
  .brand__mark {
    width: 120px; height: 120px; margin: 0 auto 6px;
    border: 3px solid var(--ink); border-radius: 50%;
  }
  .brand__name {
    font-family: "Roboto Condensed", sans-serif;
    font-weight: 500; color: var(--ink);
    line-height: 1;
  }
  .brand__name-main { display: block; font-size: 80px; letter-spacing: 12px; padding-left: 12px; }
  .brand__name-sub { display: block; font-size: 28px; letter-spacing: 14px; padding-left: 14px; margin-top: 4px; }
  .brand__tagline {
    margin-top: 12px;
    font-family: "Open Sans", sans-serif; font-style: italic;
    font-size: 19px; color: var(--tagline-blue);
  }
  .website {
    position: absolute; left: 0; right: 0; top: 366px;
    text-align: center;
    font-family: "Roboto", sans-serif; font-weight: 500;
    font-size: 31px; color: var(--white); letter-spacing: 0.5px;
  }
  .contact {
    position: absolute; left: 0; right: 0; top: 480px;
    display: flex; justify-content: center; gap: 34px;
    font-family: "Roboto Condensed", sans-serif; font-size: 33px; color: var(--white);
  }
  .contact__item { display: flex; align-items: center; gap: 10px; }
  .contact__icon { width: 42px; height: 42px; flex: none; }
  .address {
    position: absolute; left: 0; right: 0; top: 538px;
    text-align: center;
    font-family: "Roboto Condensed", sans-serif; font-size: 33px; color: var(--white);
  }
</style>
</head>
<body>
  <div class="card">
    <svg class="card__bands" viewBox="0 0 1000 640" width="1000" height="640" aria-hidden="true">
      <defs>
        <linearGradient id="blueBand" x1="0" y1="0" x2="1" y2="0">
          <stop offset="0" stop-color="var(--brand-blue-light)"/>
          <stop offset="1" stop-color="var(--brand-blue)"/>
        </linearGradient>
      </defs>
      <path d="M0 458 Q500 246 1000 458 L1000 640 L0 640 Z" fill="var(--band-dark)"/>
      <path d="M0 527 Q500 305 1000 527 L1000 640 L0 640 Z" fill="url(#blueBand)"/>
    </svg>

    <div class="brand">
      <div class="brand__mark"></div>
      <div class="brand__name">
        <span class="brand__name-main">LUMIVALE</span>
        <span class="brand__name-sub">ASSOCIATES Ltd</span>
      </div>
      <p class="brand__tagline">Thoughtful Care. Steady Hands. Bright Futures.</p>
    </div>

    <div class="website">LumivaleAssoc.net</div>

    <div class="contact">
      <div class="contact__item">
        <svg class="contact__icon" viewBox="0 0 42 42" aria-hidden="true">
          <circle cx="21" cy="20" r="18" fill="var(--white)"/>
          <path d="M8 36 L12 28 L17 33 Z" fill="var(--white)"/>
          <path d="M15 12 c-2 2 -2 5 1 9 c3 4 6 6 9 6 l2-3 -4-3 -2 2 c-2-1-4-3-5-5 l2-2 -3-4 z" fill="var(--brand-blue)"/>
        </svg>
        <span>(855) 555-0148</span>
      </div>
      <div class="contact__item">
        <svg class="contact__icon" viewBox="0 0 42 42" aria-hidden="true">
          <circle cx="21" cy="20" r="18" fill="var(--white)"/>
          <path d="M8 36 L12 28 L17 33 Z" fill="var(--white)"/>
          <text x="21" y="27" text-anchor="middle" font-family="Roboto, sans-serif" font-size="20" fill="var(--brand-blue)">@</text>
        </svg>
        <span>Lumivale512@brindlemail.net</span>
      </div>
    </div>

    <div class="address">412 Alder Crest Rd, Suite 310, Maplewood, OH&nbsp; 44190</div>
  </div>
</body>
</html>
```